Quality spirits brand needs a bottle design and logo

Designs look the same

We have received 3 designs. The font options for both of these were good, and we liked them. However, the image used wasn't strong enough. we want an image that speaks strongly in black and white, to do that it needs to be simplified some with less fine detail. We would also like to ensure some space is left for the type of spirit in the bottle i.e. RUM, SPICED RUM, VODKA, GIN

Please read the brief we have posted with the project closely to ensure you get a good understanding of what we are after.

```html
<!DOCTYPE html>
<html lang="en">
<head>
<meta charset="utf-8">
<title>Wayward Needle Distillers – Spirit Labels</title>
<link rel="stylesheet" href="https://fonts.googleapis.com/css2?family=Saira:wght@500;600;700&family=Saira+Condensed:wght@500;600&display=swap">
<style>
  :root {
    --backdrop: #050608;
    --glass: #c3c9d0;
    --glass-edge: #e2e6ea;
    --spiced-tint: #9a4f5a;
    --ink: #1c2b5a;
    --tag-paper: #ece5cf;
    --tag-ink: #2a2f45;
    --tag-red: #b3262b;
    --tag-gold: #d99a2b;
  }
  * { margin: 0; padding: 0; box-sizing: border-box; }
  html, body { width: 1200px; height: 900px; overflow: hidden; background: var(--backdrop); }
  .range {
    position: relative; width: 1200px; height: 900px;
    display: flex; justify-content: center; gap: 10px; padding-left: 0;
  }
  .label { width: 300px; height: 900px; display: block; }
  .brand-name { font-family: "Saira", sans-serif; font-weight: 700; font-size: 17px; fill: var(--ink); letter-spacing: 1px; }
  .batch-word { font-family: "Saira", sans-serif; font-weight: 700; font-size: 12px; fill: var(--ink); letter-spacing: 1px; }
  .spirit-name { font-family: "Saira", sans-serif; font-weight: 700; font-size: 46px; fill: var(--ink); letter-spacing: 1px; }
  .spirit-note { font-family: "Saira Condensed", sans-serif; font-weight: 600; font-size: 11px; fill: var(--ink); letter-spacing: 1px; }
  .volume { font-family: "Saira", sans-serif; font-weight: 700; font-size: 14px; fill: var(--ink); letter-spacing: 1px; }
  .tagline { font-family: "Saira", sans-serif; font-weight: 700; font-size: 14px; fill: var(--ink); letter-spacing: 1.5px; }
  .tag-small { font-family: "Saira Condensed", sans-serif; font-weight: 600; font-size: 5.5px; fill: var(--tag-ink); letter-spacing: .3px; }
  .tag-abv { font-family: "Saira", sans-serif; font-weight: 700; font-size: 13px; fill: var(--tag-red); }
  .tag-abv-unit { font-family: "Saira", sans-serif; font-weight: 600; font-size: 6px; fill: var(--tag-red); letter-spacing: 1px; }
</style>
</head>
<body>
<main class="range">

  <!-- White Rum -->
  <svg class="label label--white-rum" viewBox="0 0 300 900" aria-label="White Rum label">
    <defs>
      <path id="arc-white" d="M 33 585 A 117 117 0 0 0 267 585"/>
    </defs>
    <rect class="glass" x="20" y="300" width="260" height="560" rx="34" fill="var(--glass)"/>
    <circle class="brand-dot" cx="150" cy="418" r="12" fill="var(--ink)"/>
    <text class="brand-name" x="150" y="458" text-anchor="middle">WAYWARD NEEDLE</text>
    <text class="brand-name" x="150" y="480" text-anchor="middle">DISTILLERS</text>
    <text class="batch-word" x="48" y="558">SMALL</text>
    <text class="batch-word" x="252" y="558" text-anchor="end">BATCH</text>
    <text class="tagline"><textPath href="#arc-white" startOffset="50%" text-anchor="middle">NOT ALL WHO WANDER ARE AIMLESS</textPath></text>
    <text class="spirit-name" x="150" y="614" text-anchor="middle">WHITE</text>
    <text class="spirit-name" x="150" y="652" text-anchor="middle">RUM</text>
    <text class="volume" x="150" y="672" text-anchor="middle">700 ML</text>
    <g class="batch-tag" transform="translate(38 722) rotate(-2)">
      <rect width="225" height="74" fill="var(--tag-paper)"/>
      <rect x="4" y="4" width="217" height="66" fill="none" stroke="var(--tag-ink)" stroke-width=".5"/>
      <circle cx="26" cy="37" r="18" fill="var(--tag-gold)"/>
      <text class="tag-small" x="55" y="14">MASTER DISTILLER</text>
      <line x1="55" y1="30" x2="125" y2="30" stroke="var(--tag-ink)" stroke-width=".5"/>
      <text class="tag-abv" x="131" y="24">40%</text>
      <text class="tag-abv-unit" x="135" y="32">ABV</text>
      <text class="tag-small" x="163" y="17">BATCH 0000</text>
      <text class="tag-small" x="163" y="29">BOTTLE #0000</text>
      <text class="tag-small" x="55" y="44">DISTILLED IN SMALL COPPER POTS AND RESTED</text>
      <text class="tag-small" x="55" y="52">WITH CARE BEFORE BOTTLING BY HAND</text>
      <text class="tag-small" x="55" y="60">EACH SEASON.</text>
    </g>
  </svg>

  <!-- Spiced Rum -->
  <svg class="label label--spiced-rum" viewBox="0 0 300 900" aria-label="Spiced Rum label">
    <defs>
      <path id="arc-spiced" d="M 33 585 A 117 117 0 0 0 267 585"/>
      <linearGradient id="spiced-glass" x1="0" y1="0" x2="0" y2="1">
        <stop offset="0" stop-color="var(--spiced-tint)"/>
        <stop offset="1" stop-color="#b79aa0"/>
      </linearGradient>
    </defs>
    <rect class="glass" x="20" y="300" width="260" height="560" rx="34" fill="url(#spiced-glass)"/>
    <circle class="brand-dot" cx="150" cy="418" r="12" fill="var(--ink)"/>
    <text class="brand-name" x="150" y="458" text-anchor="middle">WAYWARD NEEDLE</text>
    <text class="brand-name" x="150" y="480" text-anchor="middle">DISTILLERS</text>
    <text class="batch-word" x="48" y="558">SMALL</text>
    <text class="batch-word" x="252" y="558" text-anchor="end">BATCH</text>
    <text class="tagline"><textPath href="#arc-spiced" startOffset="50%" text-anchor="middle">NOT ALL WHO WANDER ARE AIMLESS</textPath></text>
    <text class="spirit-name" x="150" y="614" text-anchor="middle">SPICED</text>
    <text class="spirit-name" x="150" y="652" text-anchor="middle">RUM</text>
    <text class="volume" x="150" y="672" text-anchor="middle">700 ML</text>
    <g class="batch-tag" transform="translate(38 722) rotate(-2)">
      <rect width="225" height="74" fill="var(--tag-paper)"/>
      <rect x="4" y="4" width="217" height="66" fill="none" stroke="var(--tag-ink)" stroke-width=".5"/>
      <circle cx="26" cy="37" r="18" fill="var(--tag-gold)"/>
      <text class="tag-small" x="55" y="14">MASTER DISTILLER</text>
      <line x1="55" y1="30" x2="125" y2="30" stroke="var(--tag-ink)" stroke-width=".5"/>
      <text class="tag-abv" x="131" y="24">40%</text>
      <text class="tag-abv-unit" x="135" y="32">ABV</text>
      <text class="tag-small" x="163" y="17">BATCH 0000</text>
      <text class="tag-small" x="163" y="29">BOTTLE #0000</text>
      <text class="tag-small" x="55" y="44">DISTILLED IN SMALL COPPER POTS AND RESTED</text>
      <text class="tag-small" x="55" y="52">WITH CARE BEFORE BOTTLING BY HAND</text>
      <text class="tag-small" x="55" y="60">EACH SEASON.</text>
    </g>
  </svg>

  <!-- Vodka -->
  <svg class="label label--vodka" viewBox="0 0 300 900" aria-label="Vodka label">
    <defs>
      <path id="arc-vodka" d="M 33 585 A 117 117 0 0 0 267 585"/>
    </defs>
    <rect class="glass" x="20" y="300" width="260" height="560" rx="34" fill="var(--glass)"/>
    <circle class="brand-dot" cx="150" cy="418" r="12" fill="var(--ink)"/>
    <text class="brand-name" x="150" y="458" text-anchor="middle">WAYWARD NEEDLE</text>
    <text class="brand-name" x="150" y="480" text-anchor="middle">DISTILLERS</text>
    <text class="batch-word" x="48" y="558">SMALL</text>
    <text class="batch-word" x="252" y="558" text-anchor="end">BATCH</text>
    <text class="tagline"><textPath href="#arc-vodka" startOffset="50%" text-anchor="middle">NOT ALL WHO WANDER ARE AIMLESS</textPath></text>
    <text class="spirit-name" x="150" y="614" text-anchor="middle">VODKA</text>
    <text class="spirit-note" x="150" y="635" text-anchor="middle">NON CHILL-FILTERED</text>
    <text class="spirit-note" x="150" y="648" text-anchor="middle">HAND DISTILLED</text>
    <text class="volume" x="150" y="672" text-anchor="middle">700 ML</text>
    <g class="batch-tag" transform="translate(38 722) rotate(-2)">
      <rect width="225" height="74" fill="var(--tag-paper)"/>
      <rect x="4" y="4" width="217" height="66" fill="none" stroke="var(--tag-ink)" stroke-width=".5"/>
      <circle cx="26" cy="37" r="18" fill="var(--tag-gold)"/>
      <text class="tag-small" x="55" y="14">MASTER DISTILLER</text>
      <line x1="55" y1="30" x2="125" y2="30" stroke="var(--tag-ink)" stroke-width=".5"/>
      <text class="tag-abv" x="131" y="24">40%</text>
      <text class="tag-abv-unit" x="135" y="32">ABV</text>
      <text class="tag-small" x="163" y="17">BATCH 0000</text>
      <text class="tag-small" x="163" y="29">BOTTLE #0000</text>
      <text class="tag-small" x="55" y="44">DISTILLED IN SMALL COPPER POTS AND RESTED</text>
      <text class="tag-small" x="55" y="52">WITH CARE BEFORE BOTTLING BY HAND</text>
      <text class="tag-small" x="55" y="60">EACH SEASON.</text>
    </g>
  </svg>

</main>
</body>
</html>
```